Harwick Market
Your Authentic Market Experience
Project: Harwick Market
Harwick Market - Events
Creative Brief
Bright & Fun-filled
we will not be putting a name on the card
we will not be putting an address on the card
harwickmarketmanager@plovenmail.com
www.harwickfarmersmarket-example.com
Saturdays 2pm-4pm May long weekend - September long weekend
We haven't got a specific idea for the back of the card. We just know that we like the look of double sided cards
QJMDesignworks QJMDesignworks
DorvalTownStalls DorvalTownStalls

```html
<!DOCTYPE html>
<html lang="en">
<head>
<meta charset="utf-8">
<title>Harwick Market – Stationery</title>
<link rel="stylesheet" href="https://fonts.googleapis.com/css2?family=Montserrat:wght@500;600;700&family=Open+Sans:wght@400;600&display=swap">
<style>
  :root{
    --bg:#e8e5e1;
    --paper:#ffffff;
    --green:#8cc63f;
    --green-dark:#74a92e;
    --charcoal:#3b3b3d;
    --ink:#4a4a4a;
    --muted:#8a8a8a;
    --rule:#d9d9d9;
  }
  *{box-sizing:border-box;margin:0;padding:0}
  html,body{width:1200px;height:897px;overflow:hidden;background:var(--bg)}
  body{position:relative;font-family:"Open Sans",Arial,sans-serif;color:var(--ink)}

  .brand{display:flex;align-items:center;gap:6px}
  .brand-dot{border-radius:50%;background:var(--green);flex:none}
  .brand-name{font-family:"Montserrat",Arial,sans-serif;font-weight:700;color:var(--charcoal);letter-spacing:.3px}

  .contact-list{list-style:none}
  .contact-list li{display:flex;align-items:center;gap:6px;font-size:8.5px;color:var(--ink);line-height:1}
  .contact-list svg{flex:none}

  /* Letterhead */
  .letterhead{position:absolute;left:213px;top:73px;width:430px;height:682px;background:var(--paper);box-shadow:0 2px 6px rgba(0,0,0,.12);overflow:hidden}
  .letterhead .brand{position:absolute;left:28px;top:30px}
  .letterhead .brand-dot{width:22px;height:22px}
  .letterhead .brand-name{font-size:22px}
  .letterhead .contact-list{position:absolute;left:176px;top:32px}
  .letterhead .contact-list li{margin-bottom:7px}
  .letter-title{position:absolute;left:30px;top:164px;font-family:"Montserrat",Arial,sans-serif;font-weight:600;font-size:26px;color:var(--green);letter-spacing:.5px}
  .letter-body{position:absolute;left:30px;top:206px;width:370px}
  .letter-body p{font-size:8.3px;line-height:1.5;margin-bottom:11px;color:#555;text-align:justify}
  .signature{position:absolute;right:40px;top:520px;text-align:left}
  .signature-name{font-family:"Montserrat",Arial,sans-serif;font-size:11px;font-weight:500;color:var(--green)}
  .signature-role{font-size:6.5px;color:var(--muted);text-transform:uppercase;letter-spacing:.5px}
  .letter-wave{position:absolute;left:0;bottom:0;width:430px;height:96px}

  /* Envelope */
  .envelope{position:absolute;left:666px;top:230px;width:400px;height:255px;background:var(--paper);box-shadow:0 2px 6px rgba(0,0,0,.12);overflow:hidden}
  .envelope-flap{position:absolute;left:0;top:0;width:400px;height:84px}
  .envelope .brand{position:absolute;left:56px;top:26px}
  .envelope .brand-dot{width:13px;height:13px}
  .envelope .brand-name{font-size:14px;color:var(--paper)}
  .envelope .contact-list{position:absolute;left:22px;top:196px}
  .envelope .contact-list li{font-size:5.5px;gap:4px;margin-bottom:4px}

  /* Business cards */
  .card{position:absolute;left:666px;width:206px;height:121px;box-shadow:0 2px 5px rgba(0,0,0,.14);overflow:hidden}
  .card-front{top:557px;background:var(--paper)}
  .card-back{top:702px;background:var(--charcoal);display:flex;align-items:center;justify-content:center}
  .card-front .brand{position:absolute;right:12px;top:16px}
  .card-front .brand-dot{width:12px;height:12px}
  .card-front .brand-name{font-size:14px}
  .market-hours{position:absolute;left:12px;top:18px;width:92px}
  .market-hours-days{font-family:"Montserrat",Arial,sans-serif;font-weight:600;font-size:6.5px;color:var(--charcoal)}
  .market-hours-season{font-size:5px;line-height:1.4;color:var(--muted);margin-top:2px}
  .card-wave{position:absolute;left:0;bottom:0;width:206px;height:62px}
  .card-front .contact-list{position:absolute;left:104px;top:76px}
  .card-front .contact-list li{font-size:4.6px;color:var(--paper);gap:3px;margin-bottom:3px}
  .card-back .brand-dot{width:18px;height:18px}
  .card-back .brand-name{font-size:20px;color:var(--paper)}
</style>
</head>
<body>

<!-- Letterhead -->
<section class="letterhead">
  <div class="brand"><span class="brand-dot"></span><span class="brand-name">Harwick</span></div>
  <ul class="contact-list">
    <li><svg width="10" height="10" viewBox="0 0 10 10"><circle cx="5" cy="5" r="5" fill="#8cc63f"/><path d="M3.3 2.6l1 .9-.5.7a3.6 3.6 0 0 0 1.9 1.9l.7-.5.9 1-.7.8C4.9 7.3 2.7 5.1 2.6 3.2z" fill="#fff"/></svg>555-014-2297</li>
    <li><svg width="10" height="10" viewBox="0 0 10 10"><circle cx="5" cy="5" r="5" fill="#8cc63f"/><rect x="2.5" y="3.2" width="5" height="3.6" fill="none" stroke="#fff" stroke-width=".7"/><path d="M2.6 3.3L5 5.2l2.4-1.9" fill="none" stroke="#fff" stroke-width=".7"/></svg>harwickmarketmanager@plovenmail.com</li>
    <li><svg width="10" height="10" viewBox="0 0 10 10"><circle cx="5" cy="5" r="5" fill="#8cc63f"/><circle cx="5" cy="5" r="2.6" fill="none" stroke="#fff" stroke-width=".6"/><path d="M2.4 5h5.2M5 2.4c-1.3 1.5-1.3 3.7 0 5.2M5 2.4c1.3 1.5 1.3 3.7 0 5.2" fill="none" stroke="#fff" stroke-width=".5"/></svg>www.harwickfarmersmarket-example.com</li>
  </ul>

  <h1 class="letter-title">LOREM IPSUM</h1>
  <div class="letter-body">
    <p>Thank you for joining us at the market this season. Our stalls bring fresh produce, baked goods and local crafts together every Saturday afternoon. We look forward to welcoming families, neighbours and visitors to enjoy live music, friendly vendors and the warm spirit of our growing community.</p>
    <p>Vendors are asked to arrive early to set up their tables before the gates open. Please keep walkways clear and bring your own shade. Parking is available beside the hall, and volunteers will help with unloading where needed. Any questions can be sent to our market manager by email.</p>
    <p>We thank every grower and maker for their support and hope to see you soon.</p>
  </div>
  <div class="signature">
    <div class="signature-name">Lorem Ipsum</div>
    <div class="signature-role">Market Manager</div>
  </div>

  <svg class="letter-wave" viewBox="0 0 430 96" preserveAspectRatio="none">
    <path d="M0 40 C110 10 230 70 430 22 L430 96 L0 96 Z" fill="#3b3b3d"/>
    <path d="M0 52 C120 24 240 84 430 36 L430 96 L0 96 Z" fill="#8cc63f"/>
  </svg>
</section>

<!-- Envelope -->
<section class="envelope">
  <svg class="envelope-flap" viewBox="0 0 400 84" preserveAspectRatio="none">
    <path d="M0 0 H400 V58 C300 84 120 50 0 76 Z" fill="#3b3b3d"/>
    <path d="M0 76 C120 50 300 84 400 58 V62 C300 88 120 54 0 80 Z" fill="#8cc63f"/>
  </svg>
  <div class="brand"><span class="brand-dot"></span><span class="brand-name">Harwick</span></div>
  <ul class="contact-list">
    <li><svg width="6" height="6" viewBox="0 0 10 10"><circle cx="5" cy="5" r="5" fill="#8cc63f"/></svg>555-014-2297</li>
    <li><svg width="6" height="6" viewBox="0 0 10 10"><circle cx="5" cy="5" r="5" fill="#8cc63f"/></svg>harwickmarketmanager@plovenmail.com</li>
    <li><svg width="6" height="6" viewBox="0 0 10 10"><circle cx="5" cy="5" r="5" fill="#8cc63f"/></svg>www.harwickfarmersmarket-example.com</li>
  </ul>
</section>

<!-- Business card front -->
<section class="card card-front">
  <div class="market-hours">
    <div class="market-hours-days">Saturdays 2pm-4pm</div>
    <div class="market-hours-season">May long weekend – September long weekend</div>
  </div>
  <div class="brand"><span class="brand-dot"></span><span class="brand-name">Harwick</span></div>
  <svg class="card-wave" viewBox="0 0 206 62" preserveAspectRatio="none">
    <path d="M0 24 C60 4 120 38 206 8 L206 62 L0 62 Z" fill="#3b3b3d"/>
    <path d="M0 30 C60 12 120 44 206 16 L206 62 L0 62 Z" fill="#8cc63f"/>
  </svg>
  <ul class="contact-list">
    <li>555-014-2297</li>
    <li>harwickmarketmanager@plovenmail.com</li>
    <li>www.harwickfarmersmarket-example.com</li>
  </ul>
</section>

<!-- Business card back -->
<section class="card card-back">
  <div class="brand"><span class="brand-dot"></span><span class="brand-name">Harwick</span></div>
</section>

</body>
</html>
```